Designing a brochures for an educational counseling service provider

We would like a 4 sided design on a 11x8.5 paper, half folded. I have including a sample design we did to give you an idea of what we envision but we welcome creativity to make beautiful looking flyers. Text for the flier is included as well as our logo.
- The most important thing is capturing our audience/market. We will be handing these flies to schools, organizations and individual clients.

www.plorvaeducationalconsultants.example

Target Market(s)

We are targeting international students wanting to study in the U.S and Canada.

Industry/Entity Type

Education

Requirements
Must have
• - Clean and clear
• - Our logo should visible and well placed.
• - Could you the pictures of students, libraries and school buildings or you could use the pictures we already have.
Nice to have
• We would like this to match business cards.

```html
<!DOCTYPE html>
<html lang="en">
<head>
<meta charset="utf-8">
<title>Plorva International Educational Consultants – Brochure</title>
<link rel="stylesheet" href="https://fonts.googleapis.com/css2?family=Didact+Gothic&family=Ubuntu:wght@400;500;700&display=swap">
<style>
  :root{
    --navy:#0f2838;
    --navy-2:#15354a;
    --orange:#f07a22;
    --orange-dark:#e2661a;
    --cream:#fbf6c9;
    --paper:#ffffff;
    --ink:#333333;
    --bg:#e6e6e6;
    --sans:"Didact Gothic", "Century Gothic", sans-serif;
    --head:"Ubuntu", Arial, sans-serif;
  }
  *{box-sizing:border-box;margin:0;padding:0}
  html,body{width:1200px;height:1200px;overflow:hidden;background:var(--bg)}
  body{position:relative;font-family:var(--sans);color:var(--ink)}
  .page{position:absolute;width:360px;height:560px;background:var(--paper);overflow:hidden;box-shadow:0 2px 8px rgba(0,0,0,.18)}
  .p-back{left:240px;top:25px}
  .p-front{left:600px;top:25px}
  .p-about{left:240px;top:615px}
  .p-services{left:600px;top:615px}
  .abs{position:absolute}
  .photo{position:absolute;left:0;width:100%}
  .corner{position:absolute;left:0;width:100%}

  /* back cover */
  .back-sky{position:absolute;left:0;top:0;width:100%;height:386px;background:linear-gradient(180deg,#f7f0b8 0%,#fdf9de 45%,#fffbe8 60%)}
  .back-tagline{top:60px;left:0;width:100%;text-align:center;font-size:12.5px;line-height:16.5px;color:#222}
  .back-photo{top:240px;height:146px;background:linear-gradient(180deg,#e9e2b6 0%,#c9b49a 45%,#8a6f5a 80%,#d8d6d0 100%)}
  .back-panel{position:absolute;left:0;top:386px;width:100%;height:160px;background:var(--navy)}
  .brand-sm{top:402px;left:0;width:100%;display:flex;justify-content:center;align-items:center;gap:6px;color:#fff;font-family:var(--head);font-weight:700;font-size:11px;letter-spacing:.5px}
  .dot{display:inline-block;border-radius:50%;background:var(--orange);flex:none}
  .contact{top:446px;left:0;width:100%;text-align:center;color:#fff;font-size:8.2px;line-height:11.3px}
  .contact .label{color:var(--orange);font-family:var(--head);font-weight:700;font-size:8px}
  .contact b{font-family:var(--head);font-weight:700}

  /* front cover */
  .brand-lg{top:72px;left:26px;width:310px;display:flex;align-items:center;gap:12px}
  .brand-lg .dot{width:52px;height:52px}
  .brand-lg .brand-text{display:flex;flex-direction:column}
  .brand-lg .brand-row{display:flex;align-items:center;gap:9px}
  .brand-lg .name{font-family:var(--head);font-weight:700;font-size:34px;color:var(--navy);line-height:1}
  .brand-lg .sub{font-family:var(--head);font-weight:700;font-size:8.5px;color:var(--navy);line-height:10.5px;letter-spacing:.2px;white-space:nowrap}
  .brand-lg .tag{font-size:6px;letter-spacing:1.7px;color:var(--navy);margin-top:5px;white-space:nowrap}
  .front-photo{top:174px;height:132px;background:linear-gradient(180deg,#3a2a22 0%,#6d4e3c 50%,#4a3b36 100%)}
  .front-panel{position:absolute;left:0;top:306px;width:100%;height:176px;background:var(--navy)}
  .front-head{top:321px;left:0;width:100%;text-align:center;color:#fff;font-size:11px;line-height:17px}
  .front-head .big{font-size:19px;letter-spacing:.3px}
  .front-head b{font-family:var(--head);font-weight:700;font-size:11.2px}
  .services-row{top:412px;left:10px;width:340px;display:flex;justify-content:space-between}
  .svc{width:80px;text-align:center;position:relative}
  .svc .ring{width:34px;height:34px;border-radius:50%;background:#fff;border:3px solid #e8c7a8;margin:0 auto;display:flex;align-items:center;justify-content:center}
  .svc span{display:block;margin-top:7px;color:var(--orange);font-family:var(--head);font-weight:500;font-size:7.3px;white-space:nowrap}
  .svc+.svc::before{content:"";position:absolute;left:-2px;top:5px;width:1px;height:30px;background:#5d7686}
  .front-band{position:absolute;left:0;top:482px;width:100%;height:54px;background:var(--orange);text-align:center;color:#fff;padding-top:8px;font-size:10px;line-height:13px}
  .front-band b{font-family:var(--head);font-weight:700;font-size:10px}

  /* inner pages */
  .inner-photo{top:0;height:94px}
  .about-photo{background:linear-gradient(90deg,#2b2420 0%,#7a5a46 35%,#503a2e 60%,#b08866 85%,#6b5444 100%)}
  .services-photo{background:linear-gradient(180deg,#e7e4da 0%,#c8b8a4 55%,#8a6a55 100%)}
  .tab{position:absolute;top:94px;left:0;height:22px}
  .tab-text{position:absolute;top:97px;left:25px;color:#fff;font-family:var(--head);font-weight:500;font-size:12.5px}
  .copy{position:absolute;left:25px;width:312px;font-size:7.3px;line-height:9.2px;color:#333;text-align:justify}
  .copy p{margin-bottom:7px}
  .bullets{list-style:none}
  .bullets li{position:relative;padding-left:17px;margin-bottom:7px}
  .bullets li::before{content:"";position:absolute;left:0;top:2px;width:5px;height:5px;background:var(--orange)}
  .library-photo{top:321px;height:239px;background:linear-gradient(160deg,#e9e3d8 0%,#9aa0a6 35%,#4a4f66 70%,#2b2e4a 100%)}
  .quote{position:absolute;left:0;top:417px;width:100%;height:46px;background:rgba(240,122,34,.92);color:#fff;text-align:center;font-family:var(--head);font-weight:500;font-size:11.2px;line-height:15.5px;padding-top:7px}
  .svc-copy{position:absolute;left:25px;width:312px;top:121px;font-size:6.5px;line-height:7.9px;color:#333;text-align:justify}
  .svc-copy p{margin-bottom:4px}
  .svc-copy h3{color:var(--orange);font-family:var(--head);font-weight:500;font-size:9.6px;line-height:12px;margin-bottom:2px}
  .ticks{list-style:none;margin-bottom:2px}
  .ticks li{display:flex;align-items:center;gap:6px;height:12.3px;font-size:6.7px}
  .ticks svg{flex:none}
</style>
</head>
<body>

<!-- Back cover -->
<section class="page p-back">
  <div class="back-sky"></div>
  <svg class="corner" style="top:0" width="360" height="26" viewBox="0 0 360 26">
    <rect x="0" y="0" width="360" height="3" fill="var(--orange)"/>
    <polygon points="236,0 360,0 360,26 262,26" fill="var(--orange)"/>
  </svg>
  <p class="abs back-tagline">A Full-service<br>International Educational Consulting Group<br>Serving Student And<br>Families Across The Globe.</p>
  <div class="photo back-photo" role="img" aria-label="Photo of smiling teenage girls in sports jerseys on a sports field"></div>
  <div class="back-panel"></div>
  <div class="abs brand-sm"><span class="dot" style="width:14px;height:14px"></span>PLORVA</div>
  <div class="abs contact">
    <div class="label">CONTACT US</div>
    <b>Executive Director &amp; Independent Educational Consultant</b><br>
    <span style="display:block;height:4px"></span>
    Plorva International Educational Consultants, LLC<br>
    1180 Meadow Road<br>
    Suite 3B, Fernhill, TX 75010<br>
    <span style="display:block;height:2px"></span>
    <b>Phone: 555-010-4770</b><br>
    director@plorvaeducationalconsultants.example
  </div>
  <svg class="corner" style="top:538px" width="360" height="22" viewBox="0 0 360 22">
    <rect x="0" y="0" width="360" height="22" fill="var(--navy)"/>
    <polygon points="0,8 96,8 124,22 0,22" fill="var(--orange)"/>
    <rect x="0" y="19" width="360" height="3" fill="var(--orange)"/>
  </svg>
</section>

<!-- Front cover -->
<section class="page p-front">
  <svg class="corner" style="top:0" width="360" height="26" viewBox="0 0 360 26">
    <rect x="0" y="0" width="360" height="3" fill="var(--orange)"/>
    <polygon points="0,0 124,0 96,26 0,26" fill="var(--orange)"/>
  </svg>
  <div class="abs brand-lg">
    <span class="dot"></span>
    <div class="brand-text">
      <div class="brand-row">
        <div class="name">PLORVA</div>
        <div class="sub">INTERNATIONAL<br>EDUCATIONAL<br>CONSULTANTS</div>
      </div>
      <div class="tag">INTERNATIONAL STUDENTS SOLUTIONS</div>
    </div>
  </div>
  <div class="photo front-photo" role="img" aria-label="Photo of four smiling students posing together"></div>
  <div class="front-panel"></div>
  <p class="abs front-head"><span class="big">A FULL-SERVICE</span><br><b>INTERNATIONAL EDUCATIONAL CONSULTING GROUP</b><br>SERVING STUDENT AND<br>FAMILIES ACROSS THE GLOBE.</p>
  <div class="abs services-row">
    <div class="svc">
      <div class="ring"><svg width="18" height="18" viewBox="0 0 18 18" fill="none" stroke="#555" stroke-width="1.2"><path d="M2 7 L9 3 L16 7 Z"/><path d="M4 8v6M7 8v6M11 8v6M14 8v6M2 15h14"/></svg></div>
      <span>Boarding Schools</span>
    </div>
    <div class="svc">
      <div class="ring"><svg width="18" height="18" viewBox="0 0 18 18" fill="none" stroke="#555" stroke-width="1.2"><rect x="3" y="2" width="10" height="14" rx="1"/><path d="M6 6h5M6 9h5M9 14l6-6"/></svg></div>
      <span>College Admission</span>
    </div>
    <div class="svc">
      <div class="ring"><svg width="18" height="18" viewBox="0 0 18 18" fill="none" stroke="#555" stroke-width="1.2"><circle cx="6" cy="6" r="2.3"/><circle cx="12.5" cy="7.5" r="2"/><path d="M2 15c0-3 2-4.5 4-4.5s4 1.5 4 4.5M9.5 15c0-2.3 1.4-3.6 3-3.6s3 1.3 3 3.6"/></svg></div>
      <span>Transfer Students</span>
    </div>
    <div class="svc">
      <div class="ring"><svg width="18" height="18" viewBox="0 0 18 18" fill="none" stroke="#555" stroke-width="1.2"><path d="M1.5 7 L9 3.5 L16.5 7 L9 10.5 Z"/><path d="M5 9v4c2 1.6 6 1.6 8 0V9M16.5 7v5"/></svg></div>
      <span>Graduate Students</span>
    </div>
  </div>
  <div class="front-band">
    <b>FERNHILL, TEXAS</b><br>
    <span style="display:block;height:3px"></span>
    +1-555-010-4770<br>
    info@plorvaeducationalconsultants.example
  </div>
  <svg class="corner" style="top:536px" width="360" height="24" viewBox="0 0 360 24">
    <rect x="0" y="0" width="360" height="24" fill="var(--navy)"/>
    <polygon points="0,0 262,0 236,14 0,14" fill="var(--orange)"/>
  </svg>
</section>

<!-- About page -->
<section class="page p-about">
  <div class="photo inner-photo about-photo" role="img" aria-label="Photo of three students reading together in a library"></div>
  <svg class="tab" width="130" height="22" viewBox="0 0 130 22"><polygon points="0,0 130,0 105,22 0,22" fill="var(--orange)"/></svg>
  <div class="tab-text">About Us</div>
  <div class="copy" style="top:127px">
    <p>Our mission is to make quality education accessible and affordable to the families we serve. Our services are designed with the child's future in mind. Whether one is seeking an academic or non-academic environment, it is important to us that we set our clients up for success.</p>
    <p>We are a family-centered organization and our goals are the same as those of our clients; for their child to thrive and reach their goals and dreams. With over 10 years of experience in the business, we are aware of the financial obstacles created by the ever increasing cost in education. Our expert consultants work closely with families to map out their educational budget and find the best affordable and quality educational options.</p>
    <ul class="bullets">
      <li>We are to serve you and assist you with your family's educational needs.</li>
      <li>We offer professional academic advising for boarding schools, university, transfer and graduate school and career planning educational consulting services tailored to the specfic needs of each student and each family. We support and provide guidance and assistance throughout the school and college admission process.</li>
    </ul>
  </div>
  <div class="photo library-photo" role="img" aria-label="Photo of tall curved library bookshelves seen from below"></div>
  <div class="quote">“We offer comprehensive service to families,<br>students, instituions and governmental organiztions.”</div>
</section>

<!-- Services page -->
<section class="page p-services">
  <div class="photo inner-photo services-photo" role="img" aria-label="Photo of smiling teenage girls in sports jerseys on a sports field"></div>
  <svg class="tab" width="130" height="22" viewBox="0 0 130 22"><polygon points="0,0 130,0 105,22 0,22" fill="var(--orange)"/></svg>
  <div class="tab-text">Services</div>
  <div class="svc-copy">
    <p>Finding the right school or program for your child is one of the most important decisions your family will make. The right choice will make a major impact on your child's future.</p>
    <h3>Ourpackage includes :</h3>
    <ul class="ticks">
      <li><svg width="8" height="8" viewBox="0 0 8 8"><rect x=".5" y=".5" width="7" height="7" fill="none" stroke="#333"/><path d="M1.8 4l1.6 1.6L6.6 1.5" fill="none" stroke="#333" stroke-width="1.2"/></svg>Intake interview</li>
      <li><svg width="8" height="8" viewBox="0 0 8 8"><rect x=".5" y=".5" width="7" height="7" fill="none" stroke="#333"/><path d="M1.8 4l1.6 1.6L6.6 1.5" fill="none" stroke="#333" stroke-width="1.2"/></svg>Present range of options based on needs and goals of the family</li>
      <li><svg width="8" height="8" viewBox="0 0 8 8"><rect x=".5" y=".5" width="7" height="7" fill="none" stroke="#333"/><path d="M1.8 4l1.6 1.6L6.6 1.5" fill="none" stroke="#333" stroke-width="1.2"/></svg>Interview coaching</li>
      <li><svg width="8" height="8" viewBox="0 0 8 8"><rect x=".5" y=".5" width="7" height="7" fill="none" stroke="#333"/><path d="M1.8 4l1.6 1.6L6.6 1.5" fill="none" stroke="#333" stroke-width="1.2"/></svg>Assistance with application and essays</li>
      <li><svg width="8" height="8" viewBox="0 0 8 8"><rect x=".5" y=".5" width="7" height="7" fill="none" stroke="#333"/><path d="M1.8 4l1.6 1.6L6.6 1.5" fill="none" stroke="#333" stroke-width="1.2"/></svg>Updates on student progress throughout their enrollment with the school.</li>
      <li><svg width="8" height="8" viewBox="0 0 8 8"><rect x=".5" y=".5" width="7" height="7" fill="none" stroke="#333"/><path d="M1.8 4l1.6 1.6L6.6 1.5" fill="none" stroke="#333" stroke-width="1.2"/></svg>Advisement on financial documents and visa applications</li>
    </ul>
    <h3>Boarding schools :</h3>
    <p>Students who want the best out of their grade school experience are likely to choose boarding schools because they are proven to better prepare students for university.North American boarding schools provide a quality dynamic experience that will facilitate personal growth in independence, leadership, and confidence as well as provide the academic curriculum necessary to prepare students for university.</p>
    <h3>College admission :</h3>
    <p>As Educational Consultants, we specialize in college/university admissions and we understand how confusing, time-consuming, and stressful the application process can be. Our experienced counselors are here to answer your questions and guide you step by step. As Parents and students may have limited access to information on schools, may not know or understand the entire process as a whole, nor where/how to begin, our experts counselors have a solutions.</p>
    <p>Clients increase the odds of admissions with our comprehensive plan of action. We believe that regardless of a student's level of involvement in extra-curricular activities or preparedness, they still possess something they can offer to the university; therefore we help them shine on their college applications.</p>
    <h3>Transfer students :</h3>
    <p>Need to find a school an alternative school that is a better match for you? We work with students and families to transfer from one school to another.</p>
    <h3>Scholarships :</h3>
    <p>Funding the education for your children in some of the world's top schools can be very expensive as tuition and fees increase at an average of 4% every year. We work with you to determine the budget for your family, applying to scholarship available and guide you through the financial aid process.</p>
    <p>Over 70% of our clients have been awarded scholarships or Financial Aid, making your education goals attainable an affordable and your children education possible.</p>
    <p>Include at the bottom of last page "Our consultants are members of GEAC, the leading association for educational consultants in North America."</p>
  </div>
  <svg class="corner" style="top:538px" width="360" height="22" viewBox="0 0 360 22">
    <polygon points="262,0 360,0 360,22 236,22" fill="var(--orange)"/>
    <rect x="0" y="19" width="360" height="3" fill="var(--orange)"/>
  </svg>
</section>

</body>
</html>
```